Simple Packaging Design For Camera Company

We need packaging designed for our product. Our product is a lens that fits onto smart phones, allowing better quality photos. We would like the design to be simple. Maybe the front cover with just the Tindel logo and the product name (BROAD VIEW MAX) underneath. the box color a light grey and text black. instead of having a picture of our product we were thinking of a outline sketch of it.

Target Market(s)

anyone looking to take better photos, but not wanting a DSLR

Industry/Entity Type

Digital Camera

Font styles to use
Sans Serif

Requirements
Nice to have
• - A sketch outline of the product. not too detailed
• - Light grey background and black text
Should not have
• stock images

```html
<!DOCTYPE html>
<html lang="en">
<head>
<meta charset="UTF-8">
<title>Tindel — Broad View Max packaging</title>
<link rel="stylesheet" href="https://fonts.googleapis.com/css2?family=Saira+Condensed:wght@300;500&display=swap">
<style>
  :root {
    --panel-grey: #eeeeee;
    --side-grey: #e4e4e4;
    --edge-line: #d2d2d2;
    --sketch-light: #ebebeb;
    --sketch-dark: #dcdcdc;
    --ink-black: #111111;
    --ink-grey: #7b7b7b;
  }
  html, body {
    margin: 0;
    padding: 0;
    width: 1200px;
    height: 1200px;
    overflow: hidden;
    background: var(--panel-grey);
  }
  .packaging {
    position: relative;
    width: 1200px;
    height: 1200px;
    display: flex;
    font-family: "Saira Condensed", "Arial Narrow", sans-serif;
  }

  /* Side panel with vertical wordmark */
  .box-side {
    width: 270px;
    height: 1200px;
    background: var(--side-grey);
    border-right: 2px solid var(--edge-line);
    box-sizing: border-box;
    display: flex;
    justify-content: center;
    align-items: center;
  }
  .side-lockup {
    writing-mode: vertical-rl;
    display: flex;
    flex-direction: column;
    align-items: center;
    gap: 18px;
    margin-top: 160px;
  }
  .side-brand {
    margin: 0;
    font-weight: 300;
    font-size: 130px;
    line-height: 1;
    letter-spacing: 0.34em;
    padding-block-start: 0.34em;
    text-transform: uppercase;
    color: var(--ink-black);
  }
  .side-product {
    margin: 0;
    font-weight: 500;
    font-size: 40px;
    line-height: 1;
    letter-spacing: 0.05em;
    color: var(--ink-grey);
  }

  /* Front face */
  .box-front {
    position: relative;
    flex: 1;
    height: 1200px;
    background: var(--panel-grey);
  }
  .product-sketch {
    position: absolute;
    left: 185px;
    top: 150px;
    width: 560px;
    height: 500px;
  }
  .front-brand {
    position: absolute;
    left: 0;
    right: 0;
    top: 690px;
    margin: 0;
    text-align: center;
    font-weight: 300;
    font-size: 175px;
    line-height: 1;
    letter-spacing: 0.32em;
    padding-left: 0.32em;
    text-transform: uppercase;
    color: var(--ink-black);
  }
  .front-product {
    position: absolute;
    left: 0;
    right: 0;
    top: 905px;
    margin: 0;
    text-align: center;
    font-weight: 500;
    font-size: 54px;
    line-height: 1;
    letter-spacing: 0.05em;
    color: var(--ink-grey);
  }
</style>
</head>
<body>
  <main class="packaging">
    <section class="box-side">
      <div class="side-lockup">
        <h2 class="side-brand">Tindel</h2>
        <p class="side-product">BROAD VIEW MAX</p>
      </div>
    </section>
    <section class="box-front">
      <svg class="product-sketch" viewBox="0 0 560 500" role="img" aria-label="Line sketch of the clip-on phone lens">
        <defs>
          <radialGradient id="sketchTone" cx="50%" cy="50%" r="60%">
            <stop offset="0%" stop-color="var(--sketch-light)"/>
            <stop offset="100%" stop-color="var(--sketch-dark)"/>
          </radialGradient>
        </defs>
        <rect x="0" y="0" width="560" height="500" rx="28" fill="url(#sketchTone)"/>
      </svg>
      <h1 class="front-brand">Tindel</h1>
      <p class="front-product">BROAD VIEW MAX</p>
    </section>
  </main>
</body>
</html>
```